Business card for Tolvery Anesthesia LLC

This is for a business care for Tolvery Anesthesia LLC. Dr. Lisbeth Tolvery, CRNA, DNAP is the sole provider in the LLC. Business address is 4718 N Brackley Street,
Oakhaven, PA 17342
CRNA stands for certified registered nurse anesthetist
"Keeping you safe and comfortable"
I plan to give this business card to the patients that I provide anesthesia to.
Creative design that ties into Anesthesia. Calm soothing colors.

Target Market(s)

Business card for my patients.

Industry/Entity Type

Medicine

Contact Information for Business Card

Creative, professional, eye catching

Logo Text

Tolvery Anesthesia

Font styles to use
Serif
Script

Colors

Designer to choose colors to be used in the design.

Requirements
Must have
• Tolvery Anesthesia
• Dr. Lisbeth Tolvery, CRNA, DNAP
• tolvery.anesthesia@ quillmail.net
Nice to have
• "Keeping you safe and comfortable"
Should not have
• phone number

```html
<!DOCTYPE html>
<html lang="en">
<head>
<meta charset="UTF-8">
<title>Tolvery Anesthesia — Business Card</title>
<link rel="stylesheet" href="https://fonts.googleapis.com/css2?family=Jost:wght@400;500;800&display=swap">
<style>
  :root {
    --backdrop: #2b2e31;
    --sage-dark: #b7c8a3;
    --sage-mid: #c6d4b4;
    --sage-light: #d6e0c8;
    --cream: #f8ead3;
    --paper: #ffffff;
    --ink: #111111;
    --teal-deep: #0f3b3a;
    --teal: #2e7f80;
    --avatar-bg: #c9dde0;
    --avatar-tone: #e6a47a;
  }
  html, body {
    margin: 0;
    width: 1200px;
    height: 900px;
    overflow: hidden;
    background: var(--backdrop);
    font-family: "Jost", "Futura", sans-serif;
  }
  .business-card {
    position: absolute;
    left: 75px;
    top: 150px;
    width: 1050px;
    height: 600px;
    border-radius: 36px;
    overflow: hidden;
    background: var(--paper);
    box-shadow: 0 12px 40px rgba(0,0,0,.45);
  }
  .edge-bands {
    position: absolute;
    top: 0;
    bottom: 0;
    display: flex;
  }
  .edge-bands--left { left: 0; }
  .edge-bands--right { right: 0; flex-direction: row-reverse; }
  .edge-bands span { display: block; height: 100%; }
  .band-dark { width: 48px; background: var(--sage-dark); }
  .band-mid { width: 48px; background: var(--sage-mid); }
  .band-light { width: 48px; background: var(--sage-light); }
  .band-cream { width: 56px; background: var(--cream); }

  .brand {
    position: absolute;
    right: 220px;
    top: 50px;
    text-align: right;
  }
  .brand-name {
    margin: 0;
    font-weight: 800;
    font-size: 62px;
    letter-spacing: -1px;
    line-height: 1;
    color: var(--teal-deep);
    text-transform: uppercase;
  }
  .brand-tagline {
    margin: 6px 0 0;
    font-weight: 500;
    font-size: 31px;
    color: var(--teal);
  }
  .portrait {
    position: absolute;
    left: 470px;
    top: 205px;
    width: 210px;
    height: 210px;
    border-radius: 50%;
    background: radial-gradient(circle at 50% 45%, var(--avatar-tone) 0 22%, var(--avatar-bg) 23%);
  }
  .provider-name {
    position: absolute;
    left: 235px;
    top: 430px;
    margin: 0;
    font-weight: 400;
    font-size: 40px;
    color: var(--ink);
  }
  .contact-email {
    position: absolute;
    left: 235px;
    top: 505px;
    margin: 0;
    display: flex;
    align-items: center;
    gap: 12px;
    font-size: 30px;
    color: var(--ink);
  }
  .contact-email svg { width: 18px; height: 18px; }
</style>
</head>
<body>
  <article class="business-card">
    <div class="edge-bands edge-bands--left">
      <span class="band-dark"></span><span class="band-mid"></span><span class="band-light"></span><span class="band-cream"></span>
    </div>
    <div class="edge-bands edge-bands--right">
      <span class="band-dark"></span><span class="band-mid"></span><span class="band-light"></span><span class="band-cream"></span>
    </div>

    <header class="brand">
      <h1 class="brand-name">Tolvery Anesthesia</h1>
      <p class="brand-tagline">Keeping you safe and comfortable</p>
    </header>

    <div class="portrait" role="img" aria-label="Illustrated portrait of the provider in a white coat"></div>

    <p class="provider-name">Dr. Lisbeth Tolvery, CRNA, DNAP</p>
    <p class="contact-email">
      <svg viewBox="0 0 18 18" aria-hidden="true"><circle cx="9" cy="9" r="8" fill="#111111"/></svg>
      tolvery.anesthesia@ quillmail.net
    </p>
  </article>
</body>
</html>
```